Revamp Flyers to be engaging , fun & attractive

We want our service information flyers to be updated to match our recent design updates. Examples of the design can be seen in the two pull-up banners that have been uploaded into the brief. All the information will stay the same, but we would like the flyers to be tri-fold A4 rather than A5. Please use the range of stock and independent images within the brief. Pick one brochure to start your design. There are 7 flyers in total in this project.

Target Market(s)

Individuals with disability and their families

Industry/Entity Type

Disability Service Provider

Colors

Designer to choose colors to be used in the design.

Requirements
Must have
• Similar colours, shapes, and designs as our new banners
Nice to have
• Design and colours make the flyers easy to read

```html
<!DOCTYPE html>
<html lang="en">
<head>
<meta charset="utf-8">
<title>Brightvale – Tri-fold Service Brochure</title>
<link rel="stylesheet" href="https://fonts.googleapis.com/css2?family=Baloo+2:wght@600;800&family=Open+Sans:wght@400;600&display=swap">
<style>
  :root{
    --orange:#f39a1e;
    --yellow:#fbc829;
    --navy:#1f1d3d;
    --pink:#e6357d;
    --blue:#2aa5dd;
    --purple:#6a3fa3;
    --white:#ffffff;
    --ink:#2b2b3a;
    --stage:#e9e9ec;
    --photo-warm:#c99a7a;
    --photo-cool:#8fb3c9;
  }
  *{margin:0;padding:0;box-sizing:border-box}
  html,body{width:849px;height:1200px;overflow:hidden;background:var(--stage)}
  body{position:relative;font-family:"Open Sans",sans-serif;color:var(--ink)}
  .spread{position:absolute;left:24px;width:801px;height:566px;display:flex;box-shadow:0 4px 14px rgba(0,0,0,.18);overflow:hidden}
  .spread--outside{top:24px}
  .spread--inside{top:610px}
  .panel{position:relative;width:267px;height:100%;overflow:hidden}
  .heading{font-family:"Baloo 2",sans-serif;font-weight:800;text-transform:uppercase;line-height:1.05}
  .body{font-size:7.2px;line-height:1.45}
  .photo{position:absolute}
  .wordmark{font-family:"Open Sans",sans-serif;font-weight:600;font-size:26px;letter-spacing:0;text-align:center}

  /* outside: services panel */
  .services{background:linear-gradient(180deg,var(--orange),var(--yellow));}
  .services .heading{color:var(--white);font-size:22px;text-align:center;margin-top:34px}
  .services ul{list-style:none;text-align:center;margin-top:10px;color:var(--white);font-weight:600;font-size:9.5px;line-height:1.75}
  .services .splash{position:absolute;left:-20px;top:310px;width:310px;height:280px;background:var(--blue);border-radius:48% 52% 0 0/40% 40% 0 0}
  .services .photo{left:10px;top:300px;width:250px;height:210px;border-radius:46% 54% 50% 50%/50% 50% 50% 50%;background:linear-gradient(160deg,var(--photo-cool),var(--photo-warm))}

  /* outside: contact panel */
  .contact{background:var(--white)}
  .contact .wordmark{position:absolute;top:112px;left:0;right:0;color:var(--navy)}
  .contact .splash{position:absolute;left:40px;width:200px;background:var(--blue);color:var(--white);text-align:center;border-radius:40% 60% 45% 55%/55% 45% 55% 45%;padding:18px 16px}
  .contact .splash--touch{top:250px}
  .contact .splash--info{top:360px;background:var(--navy)}
  .contact .splash .heading{font-size:14px;margin-bottom:6px}
  .contact .line{display:flex;align-items:center;justify-content:center;gap:5px;font-size:8px;line-height:1.7}
  .contact .line svg{width:8px;height:8px;fill:var(--white)}

  /* outside: cover panel */
  .cover{background:var(--navy);color:var(--white)}
  .cover .wordmark{position:absolute;top:44px;left:0;right:0;color:var(--white)}
  .cover .tagline{position:absolute;top:92px;right:26px;text-align:right;font-family:"Baloo 2",sans-serif;font-weight:600;font-size:16px;line-height:1.1;color:var(--yellow)}
  .cover .photo{left:0;top:170px;width:267px;height:215px;background:linear-gradient(180deg,var(--photo-cool),var(--photo-warm))}
  .cover .band{position:absolute;left:0;top:385px;width:267px;background:var(--pink);padding:14px 22px;font-family:"Baloo 2",sans-serif;font-weight:600;font-size:12.5px;line-height:1.15;text-align:center}

  /* inside: about panel */
  .about{background:var(--white);padding:26px 20px}
  .about .body{margin-bottom:10px}
  .about .tag{display:inline-block;padding:4px 12px;border-radius:14px;color:var(--white);font-size:12px;margin-bottom:8px}
  .tag--blue{background:var(--blue)}
  .tag--purple{background:var(--purple)}
  .about ul{list-style:none;margin-bottom:12px}
  .about li{display:flex;gap:6px;align-items:center;font-size:7.6px;font-weight:600;line-height:1.8;text-transform:uppercase}
  .about li svg{width:8px;height:8px;fill:var(--blue)}
  .about .photo{left:0;bottom:0;width:267px;height:100px;background:linear-gradient(180deg,var(--photo-warm),var(--yellow))}

  /* inside: activities panel */
  .activities{background:var(--white)}
  .activities .photo{left:0;top:0;width:267px;height:150px;background:linear-gradient(180deg,var(--photo-cool),var(--photo-warm))}
  .activities .title{position:absolute;top:120px;left:14px;right:14px;background:var(--pink);color:var(--white);padding:8px 12px;border-radius:14px;font-size:14px}
  .activities .text{position:absolute;top:188px;left:20px;right:20px}
  .activities .text .body{margin-bottom:8px}
  .activities .weekend{position:absolute;left:0;bottom:0;width:267px;height:150px;background:var(--yellow);padding:16px 20px}
  .activities .weekend .heading{font-size:14px;color:var(--navy);margin-bottom:6px}

  /* inside: support panel */
  .support{background:var(--navy);color:var(--white);padding:22px 20px}
  .support .heading{font-size:17px;margin-bottom:6px}
  .support .heading--yellow{color:var(--yellow)}
  .support .heading--pink{color:var(--pink)}
  .support .photo{position:relative;width:227px;height:100px;border-radius:10px;margin:10px 0 14px}
  .support .photo--one{background:linear-gradient(160deg,var(--photo-warm),var(--photo-cool))}
  .support .photo--two{background:linear-gradient(160deg,var(--photo-cool),var(--photo-warm));height:110px}
</style>
</head>
<body>

<section class="spread spread--outside">
  <div class="panel services">
    <h2 class="heading">Our Services</h2>
    <ul>
      <li>Social &amp; Living Skills Programs</li>
      <li>Weekend &amp; Friday Night Outings</li>
      <li>Support Workers</li>
      <li>Respite, Supported Holidays &amp; SIL</li>
      <li>Exercise Physiology</li>
      <li>Occupational Therapy</li>
      <li>Speech Therapy</li>
      <li>Psychology</li>
      <li>Behaviour Therapy</li>
    </ul>
    <div class="splash"></div>
    <div class="photo" role="img" aria-label="Photo of a smiling group of friends outdoors"></div>
  </div>

  <div class="panel contact">
    <p class="wordmark">Brightvale</p>
    <div class="splash splash--touch">
      <h3 class="heading">Get in Touch</h3>
      <p class="line"><svg viewBox="0 0 10 10"><path d="M2 0h2l1 3-1.5 1a6 6 0 0 0 2.5 2.5L7 5l3 1v2a2 2 0 0 1-2 2A8 8 0 0 1 0 2a2 2 0 0 1 2-2z"/></svg>1300 555 012</p>
      <p class="line">hello@brightvale.org</p>
      <p class="line"><svg viewBox="0 0 10 10"><path d="M5 0a3.5 3.5 0 0 1 3.5 3.5C8.5 6 5 10 5 10S1.5 6 1.5 3.5A3.5 3.5 0 0 1 5 0z"/></svg>12 Harbour Lane, Eastwood</p>
    </div>
    <div class="splash splash--info">
      <h3 class="heading">More Information</h3>
      <p class="line">www.brightvale.org</p>
    </div>
  </div>

  <div class="panel cover">
    <p class="wordmark">Brightvale</p>
    <p class="tagline">More Independence<br>More Choice<br>More Fun</p>
    <div class="photo" role="img" aria-label="Photo of a group joining hands in a team huddle"></div>
    <p class="band">supporting you to develop independence, helping you to engage in community, social and economic activity</p>
  </div>
</section>

<section class="spread spread--inside">
  <div class="panel about">
    <p class="body">At Brightvale we believe everyone deserves the chance to live a full and active life. Our friendly team works alongside each person and their family to build skills, confidence and lasting friendships in a safe and welcoming setting.</p>
    <p class="body">Every plan is shaped around your goals, so you choose what you do, who you do it with and how often you take part.</p>
    <span class="heading tag tag--blue">What We Do</span>
    <ul>
      <li><svg viewBox="0 0 10 10"><circle cx="5" cy="5" r="5"/></svg>Build new friendships</li>
      <li><svg viewBox="0 0 10 10"><circle cx="5" cy="5" r="5"/></svg>Learn new skills</li>
      <li><svg viewBox="0 0 10 10"><circle cx="5" cy="5" r="5"/></svg>Connect with your community</li>
      <li><svg viewBox="0 0 10 10"><circle cx="5" cy="5" r="5"/></svg>Grow with a caring team</li>
    </ul>
    <span class="heading tag tag--purple">Why Choose Us?</span>
    <p class="body">We are a registered provider with years of experience, flexible hours and staff who truly care about every person we support.</p>
    <div class="photo" role="img" aria-label="Photo of participants enjoying a group activity"></div>
  </div>

  <div class="panel activities">
    <div class="photo" role="img" aria-label="Photo of a group smiling together at a day program"></div>
    <h3 class="heading title">Social Activities, Day Programs &amp; Workshops</h3>
    <div class="text">
      <p class="body">Our day programs run all week and mix fun with learning. Join cooking classes, art sessions, music, fitness and outings around town.</p>
      <p class="body">Workshops cover money skills, travel training and healthy living, helping you gain more independence at your own pace.</p>
    </div>
    <div class="weekend">
      <h3 class="heading">Weekend &amp; Friday Nightouts</h3>
      <p class="body">Catch a movie, go bowling, enjoy dinner out or dance the night away. Our weekend and Friday night outings are a great way to relax, have fun and meet new friends with support close by.</p>
    </div>
  </div>

  <div class="panel support">
    <h3 class="heading heading--yellow">Support Workers</h3>
    <p class="body">Our trained support workers help at home and in the community, from daily tasks to appointments and hobbies, always matched to your needs.</p>
    <div class="photo photo--one" role="img" aria-label="Photo of a support worker with a participant"></div>
    <h3 class="heading heading--pink">Supported Holidays, Respite &amp; SIL</h3>
    <p class="body">Take a break with supported holidays and short stays, or live more independently with our supported living options and round-the-clock care.</p>
    <div class="photo photo--two" role="img" aria-label="Photo of a group on a supported holiday outdoors"></div>
  </div>
</section>

</body>
</html>
```